Business Card Design Project

I need the following:

Logo -
Name - Dale Prewitt
Title - Customer Experience Officer
Web - www.bvrh.net
Phone - 555-417-3068
Updates

Project Deadline Extended
Reason: I launched the project later than anticipated. I look forward to seeing your designs. Dale

Industry/Entity Type

Business

```html
<!DOCTYPE html>
<html lang="en">
<head>
<meta charset="utf-8">
<title>Brightvale Relay Hub – Business Card</title>
<link rel="stylesheet" href="https://fonts.googleapis.com/css2?family=Exo+2:wght@400;500;700;800&display=swap">
<style>
  :root {
    --backdrop: #e6e7e9;
    --card: #ffffff;
    --navy: #23305e;
    --blue: #1f6fb2;
    --ink: #111418;
    --globe-light: #eef0f6;
    --globe-mid: #d3d8e6;
  }
  * { margin: 0; padding: 0; box-sizing: border-box; }
  html, body {
    width: 1200px;
    height: 772px;
    overflow: hidden;
    background: var(--backdrop);
    font-family: "Exo 2", sans-serif;
  }
  .card {
    position: absolute;
    left: 75px;
    top: 86px;
    width: 1050px;
    height: 600px;
    background: var(--card);
    border-radius: 48px;
    overflow: hidden;
  }
  .globe-backdrop {
    position: absolute;
    left: 583px;
    top: 8px;
    width: 606px;
    height: 606px;
    border-radius: 50%;
    background: radial-gradient(circle at 40% 40%, var(--globe-light) 0%, var(--globe-mid) 100%);
    opacity: 0.85;
  }
  .brand {
    position: absolute;
    left: 112px;
    top: 76px;
    display: flex;
    align-items: center;
    gap: 38px;
  }
  .brand-mark {
    width: 132px;
    height: 132px;
    border-radius: 50%;
    background: var(--blue);
    flex-shrink: 0;
  }
  .brand-text { display: flex; flex-direction: column; }
  .brand-name {
    font-weight: 800;
    font-size: 34px;
    line-height: 30px;
    letter-spacing: 1px;
    color: var(--ink);
    text-transform: uppercase;
  }
  .brand-web {
    display: flex;
    align-items: center;
    gap: 10px;
    margin-top: 8px;
    font-weight: 700;
    font-size: 16px;
    color: var(--blue);
  }
  .brand-web::before, .brand-web::after {
    content: "";
    flex: 1;
    height: 2px;
    background: var(--blue);
  }
  .person {
    position: absolute;
    left: 71px;
    top: 325px;
  }
  .person-name {
    font-weight: 700;
    font-size: 27px;
    color: var(--navy);
    letter-spacing: 0.5px;
    text-transform: uppercase;
  }
  .person-title {
    margin-top: 4px;
    font-weight: 400;
    font-size: 17px;
    color: var(--blue);
  }
  .contact {
    position: absolute;
    top: 520px;
    display: flex;
    align-items: center;
    gap: 14px;
    font-weight: 500;
    font-size: 24px;
    color: var(--blue);
    letter-spacing: 0.5px;
  }
  .contact svg { fill: var(--navy); }
  .contact-phone { left: 74px; }
  .contact-web { left: 430px; }
</style>
</head>
<body>
  <main class="card">
    <div class="globe-backdrop" role="img" aria-label="Large faint globe backdrop"></div>

    <header class="brand">
      <div class="brand-mark"></div>
      <div class="brand-text">
        <span class="brand-name">Brightvale<br>Relay<br>Hub</span>
        <span class="brand-web">www.bvrh.net</span>
      </div>
    </header>

    <section class="person">
      <h1 class="person-name">Dale Prewitt</h1>
      <p class="person-title">Customer Experience Officer</p>
    </section>

    <p class="contact contact-phone">
      <svg width="24" height="20" viewBox="0 0 24 20" aria-hidden="true">
        <path d="M1 6 Q12 -1 23 6 L21 9 L17 7.5 L17 5 Q12 3.5 7 5 L7 7.5 L3 9 Z"/>
        <path d="M6 10 L18 10 L21 19 L3 19 Z"/>
      </svg>
      555-417-3068
    </p>

    <p class="contact contact-web">
      <svg width="24" height="22" viewBox="0 0 24 22" aria-hidden="true">
        <path d="M1 1 H23 V16 H1 Z M3 3 V14 H21 V3 Z"/>
        <rect x="10" y="16" width="4" height="3"/>
        <rect x="6" y="19" width="12" height="2"/>
      </svg>
      www.bvrh.net
    </p>
  </main>
</body>
</html>
```